Product Image Design: Climbing Past the Ceiling That Held You Back (Plus More!)

I need a product image designed for a new product I will be selling on sellvanta.com that teaches how to quickly make more money by getting a raise or promotion.

Dimensions must be 1280 x 720 pixels. The product title and subtitle are as follows:

Title: Climbing Past the Ceiling That Held You Back at Last (Plus More!)

Subtitle: A Quick Route to Bigger Salary Jumps Minus Costly Schooling or Flattering the Manager Above You

I'm looking for a design that is eye catching and communicates the idea of business success and getting paid more money from a company or employer.

The target audience is professional men in their 20s and 30s who are looking to quickly make more money and advance in their careers.

Target Market(s)

Professional men in their 20s and 30s who are looking to quickly make more money and advance in their careers.

Industry/Entity Type

Professional Service

Font styles to use
Serif

Requirements
Must have
• Title and subtitle provided in project description.

Final design in 1280 x 720 dimensions (or larger with same width to height ratio).

Eye catching font, colors and graphics, but not overly flashy.

Masculine colors (i.e. no pinks or other feminine colors).
Nice to have
• N/A
Should not have
• Feminine colors or images of women.

```html
<!DOCTYPE html>
<html lang="en">
<head>
<meta charset="utf-8">
<title>Climbing Past the Ceiling That Held You Back at Last (Plus More!)</title>
<link rel="stylesheet" href="https://fonts.googleapis.com/css2?family=Lilita+One&family=Fredoka:wght@600;700&family=Catamaran:wght@400&display=swap">
<style>
  :root {
    --ink: #1d1d1d;
    --ink-deep: #141414;
    --gold: #e8b828;
    --gold-soft: #ddb14a;
    --amber-edge: #c9771c;
    --band: rgba(118, 90, 34, 0.42);
  }
  * { margin: 0; padding: 0; box-sizing: border-box; }
  html, body {
    width: 1200px;
    height: 674px;
    overflow: hidden;
    background: var(--ink-deep);
  }
  .product-cover {
    position: relative;
    width: 1200px;
    height: 674px;
    overflow: hidden;
    background: var(--ink);
  }
  .backdrop {
    position: absolute;
    inset: 0;
    background:
      radial-gradient(ellipse at 50% 45%, #262421 0%, #1c1b1a 55%, #141414 100%);
  }
  .edge {
    position: absolute;
    left: 0;
    width: 100%;
    height: 9px;
    background: linear-gradient(90deg, #b4661a, var(--amber-edge) 40%, #d88a2a 70%, #b4661a);
  }
  .edge--top { top: 0; }
  .edge--bottom { bottom: 0; }

  .title-block {
    position: absolute;
    left: 323px;
    top: 204px;
    width: 537px;
    height: 205px;
    border: 8px solid var(--gold);
  }
  .title-block__inner {
    position: absolute;
    inset: 6px;
    border: 5px solid var(--gold);
  }
  .title-block__label {
    position: absolute;
    left: 50%;
    transform: translate(-50%, -50%);
    padding: 0 12px;
    background: #1f1e1c;
    font-family: "Fredoka", sans-serif;
    font-weight: 700;
    font-size: 27px;
    letter-spacing: 3px;
    line-height: 1;
    color: var(--ink-deep);
    white-space: nowrap;
  }
  .title-block__label span {
    display: inline-block;
    background: var(--gold);
    padding: 2px 10px;
  }
  .title-block__label--top { top: 8px; }
  .title-block__label--bottom { top: 185px; }
  .title-block__main {
    position: absolute;
    left: 0;
    right: 0;
    top: 40px;
    text-align: center;
    font-family: "Lilita One", sans-serif;
    font-size: 56px;
    line-height: 58px;
    letter-spacing: 1px;
    color: var(--gold);
    text-transform: uppercase;
  }
  .title-block__tag {
    position: absolute;
    left: 0;
    width: 1200px;
    top: 426px;
    text-align: center;
    font-family: "Fredoka", sans-serif;
    font-weight: 700;
    font-size: 20px;
    letter-spacing: 4px;
    color: var(--gold);
  }

  .subtitle-band {
    position: absolute;
    left: 0;
    top: 583px;
    width: 100%;
    height: 83px;
    background: var(--band);
    display: flex;
    align-items: center;
    justify-content: center;
  }
  .subtitle-band p {
    width: 760px;
    text-align: center;
    font-family: "Catamaran", sans-serif;
    font-weight: 400;
    font-size: 22px;
    line-height: 29px;
    color: var(--gold-soft);
  }
</style>
</head>
<body>
  <main class="product-cover">
    <div class="backdrop" role="img" aria-label="Dark scuffed paper texture scattered with faint bronze dollar sign pattern"></div>
    <div class="edge edge--top"></div>

    <section class="title-block">
      <div class="title-block__inner"></div>
      <div class="title-block__label title-block__label--top"><span>CLIMBING PAST</span></div>
      <h1 class="title-block__main">The Ceiling That<br>Held You Back</h1>
      <div class="title-block__label title-block__label--bottom"><span>AT LAST</span></div>
    </section>
    <p class="title-block__tag">(PLUS MORE!)</p>

    <div class="subtitle-band">
      <p>A Quick Route to Bigger Salary Jumps Minus Costly Schooling or Flattering the Manager Above You</p>
    </div>

    <div class="edge edge--bottom"></div>
  </main>
</body>
</html>
```